Marcelo Quintana Postcard/Rack Card

Marcelo Quintana
Tenor & Vocal Coach
mqvoice@brivamail.com
(713) 582-6031
www.voicefromthecore.com
Want two sided postcard / rack card.4" x 9"
Front - vertical - picture in t-shirt, name, title (Tenor & Vocal Coach), contact information
Back - horizontal - picture in jacket, name, title (Tenor & Vocal Coach), contact information, bio (see attachment for words)
Do not leave space for an address.
Looking for an edgy modern design!

Target Market(s)

Young adults

Requirements
Nice to have
• Will pay extra to get a complimentary business card design, two sided

```html
<!DOCTYPE html>
<html lang="en">
<head>
<meta charset="utf-8">
<title>Marcelo Quintana – Rack Card</title>
<link href="https://fonts.googleapis.com/css2?family=Lato:wght@400;700&display=swap" rel="stylesheet">
<style>
  :root{
    --bg:#c9c7ca;
    --purple:#6a3fa0;
    --ink:#241f4a;
    --cream:#e6e0bb;
    --cream-edge:#cdc398;
    --wall:#e2dcc6;
    --shirt:#9c9a98;
    --jacket:#2c3352;
  }
  *{margin:0;padding:0;box-sizing:border-box}
  html,body{width:1200px;height:799px;overflow:hidden}
  body{background:radial-gradient(ellipse at 55% 40%, #dcdadc 0%, var(--bg) 70%);font-family:'Lato',sans-serif;color:var(--ink);position:relative}

  .card{position:absolute;overflow:hidden;box-shadow:0 2px 6px rgba(0,0,0,.25)}
  .card-front{left:82px;top:43px;width:312px;height:701px}
  .card-back{left:430px;top:251px;width:698px;height:310px;
    background:radial-gradient(ellipse at 40% 45%, var(--cream) 55%, var(--cream-edge) 100%)}

  .front-art{position:absolute;inset:0}

  .name{color:var(--purple);font-weight:700;letter-spacing:-.2px;line-height:1}
  .role{color:var(--ink);line-height:1.1}

  .front-id{position:absolute;left:27px;top:540px}
  .front-id .name{font-size:21px}
  .front-id .role{font-size:15px;margin-top:4px}

  .contact{list-style:none;font-size:13px;line-height:16px;color:var(--ink)}
  .contact li{display:flex;align-items:center;gap:4px}
  .contact svg{width:13px;height:13px;flex:none}
  .front-contact{position:absolute;left:27px;top:631px}

  .back-text{position:absolute;left:29px;top:24px;width:412px}
  .back-text .name{font-size:21px}
  .back-text .role{font-size:15px;margin-top:4px}
  .bio{font-size:12.8px;line-height:15.6px;margin-top:16px}
  .bio + .bio{margin-top:15.5px}
  .cta{display:block;margin-top:15px;font-size:12.8px;color:var(--purple);text-decoration:underline}
  .back-contact{margin-top:12px}

  .back-photo{position:absolute;left:426px;top:0;width:272px;height:310px;
    background:
      linear-gradient(180deg, var(--wall) 0%, #d8cfb4 38%, #6c6f84 62%, var(--jacket) 100%);
    -webkit-mask-image:linear-gradient(90deg, transparent 0, #000 60px);
    mask-image:linear-gradient(90deg, transparent 0, #000 60px)}
</style>
</head>
<body>

<section class="card card-front">
  <svg class="front-art" viewBox="0 0 312 701" preserveAspectRatio="none">
    <defs>
      <linearGradient id="skyFill" x1="0" y1="0" x2="1" y2="1">
        <stop offset="0" stop-color="#9ed6e9"/>
        <stop offset="1" stop-color="#6eb0c8"/>
      </linearGradient>
      <linearGradient id="photoTone" x1="0" y1="0" x2="0" y2="1">
        <stop offset="0" stop-color="#e8e2cf"/>
        <stop offset=".35" stop-color="#d6d0c0"/>
        <stop offset=".6" stop-color="#9d9b9a"/>
        <stop offset="1" stop-color="#5d6784"/>
      </linearGradient>
      <linearGradient id="orangeFill" x1="0" y1="0" x2="1" y2="0">
        <stop offset="0" stop-color="#f0862a"/>
        <stop offset="1" stop-color="#d9541c"/>
      </linearGradient>
    </defs>
    <rect class="front-photo" width="312" height="490" fill="url(#photoTone)" role="img" aria-label="Photo of the tenor in a grey t-shirt, leaning on a wall and smiling"/>
    <path d="M0 349 C40 450 150 475 312 437 L312 701 L0 701 Z" fill="url(#orangeFill)"/>
    <path d="M0 373 C50 478 170 510 312 485 L312 701 L0 701 Z" fill="url(#skyFill)"/>
    <path d="M0 392 C90 470 240 500 312 601" fill="none" stroke="#ffffff" stroke-width="1.3"/>
  </svg>

  <div class="front-id">
    <h1 class="name">Marcelo Quintana</h1>
    <p class="role">Tenor &amp; Vocal Coach</p>
  </div>

  <ul class="contact front-contact">
    <li><svg viewBox="0 0 16 16"><path d="M4 1.5 6.5 5 5 6.5c.8 1.8 2.5 3.6 4.5 4.5L11 9.5l3.5 2.5-1.5 2.5C7.5 14 2 8.5 1.5 3z" fill="var(--purple)"/></svg>(713) 582-6031</li>
    <li><svg viewBox="0 0 16 16"><rect x="1.5" y="4" width="13" height="9" rx="1" fill="var(--purple)"/><path d="M1.8 4.5 8 9.5l6.2-5" fill="none" stroke="#fff" stroke-width="1.2"/></svg>mqvoice@brivamail.com</li>
    <li><svg viewBox="0 0 16 16"><g fill="none" stroke="var(--purple)" stroke-width="1.3"><circle cx="8" cy="8" r="6.5"/><ellipse cx="8" cy="8" rx="3" ry="6.5"/><path d="M1.5 8h13M2.5 5h11M2.5 11h11"/></g></svg>www.voicefromthecore.com</li>
  </ul>
</section>

<section class="card card-back">
  <div class="back-photo" role="img" aria-label="Photo of the tenor in a dark navy jacket and open white shirt"></div>

  <div class="back-text">
    <h2 class="name">Marcelo Quintana</h2>
    <p class="role">Tenor &amp; Vocal Coach</p>
    <p class="bio">Marcelo is a local singer and actor who has been working professionally around the country as a concert artist and musical theater performer.</p>
    <p class="bio">He studied at the Larkin School of Music, Bayview University and works as a vocal coach with local youths and adults in Houston area.</p>
    <p class="bio">Marcelo’s goal is to help his students master their individual instrument so that they can achieve a natural and effortless vocal production.</p>
    <a class="cta" href="#">For more information please contact Marcelo today!</a>
    <ul class="contact back-contact">
      <li><svg viewBox="0 0 16 16"><path d="M4 1.5 6.5 5 5 6.5c.8 1.8 2.5 3.6 4.5 4.5L11 9.5l3.5 2.5-1.5 2.5C7.5 14 2 8.5 1.5 3z" fill="var(--purple)"/></svg>(713) 582-6031</li>
      <li><svg viewBox="0 0 16 16"><rect x="1.5" y="4" width="13" height="9" rx="1" fill="var(--purple)"/><path d="M1.8 4.5 8 9.5l6.2-5" fill="none" stroke="#fff" stroke-width="1.2"/></svg>mqvoice@brivamail.com</li>
      <li><svg viewBox="0 0 16 16"><g fill="none" stroke="var(--purple)" stroke-width="1.3"><circle cx="8" cy="8" r="6.5"/><ellipse cx="8" cy="8" rx="3" ry="6.5"/><path d="M1.5 8h13M2.5 5h11M2.5 11h11"/></g></svg>www.voicefromthecore.com</li>
    </ul>
  </div>
</section>

</body>
</html>
```